Sign Advertisment for Condominium Development

I need a sign created that will be placed in front of a building that is being converted into a luxury condominium development.

The sign needs to say:

Two, Boutique Luxury Condominiums Delivering late 2015.

Luxury Finishes // Designer Kitchens and Bath // Each Unit over 2,000 Square Feet

Deeded Parking Included with Each Unit

To Learn More, Contact:

Marissa Talbot or Vernon Pike
(202) 555-0147
Marissa.Talbot@example-realty.com

I need a small disclaimer at the bottom stating:

These Condominium(s) have not been registered by the Office of Residential Standards and Property Oversight Bureau Tenancy Transition and Transfer Section. A Condominium Unit may be reserved on a non-binding reservation agreement, but no contract of sale or lease that is binding on the purchaser may be entered into prior to registration.

Target Market(s)

Young professionals seeking luxury condominium

Industry/Entity Type

Building

Font styles to use
Serif

Colors
00a88f
ffffff

```html
<!DOCTYPE html>
<html lang="en">
<head>
<meta charset="utf-8">
<title>Boutique Luxury Condominiums</title>
<link rel="stylesheet" href="https://fonts.googleapis.com/css2?family=Open+Sans:ital,wght@0,400;0,700;1,400&family=Libre+Baskerville:wght@400;700&family=Roboto+Condensed:wght@700&display=swap">
<style>
  :root {
    --teal: #35bbad;
    --white: #ffffff;
    --ink: #111111;
  }
  * { margin: 0; padding: 0; box-sizing: border-box; }
  html, body { width: 1200px; height: 927px; overflow: hidden; background: var(--white); }
  .sign { position: relative; width: 1200px; height: 927px; background: var(--white); overflow: hidden; }
  .header-wave { position: absolute; left: 0; top: 0; width: 1200px; height: 460px; }
  .header-wave .band { fill: var(--teal); }
  .header-wave .corner { fill: var(--white); }
  .units-flag {
    position: absolute; left: 1010px; top: 52px; width: 250px;
    transform: rotate(45deg); transform-origin: center;
    color: var(--teal); font-family: "Open Sans", sans-serif; font-weight: 700;
    text-align: center; line-height: 1;
  }
  .units-flag .count { font-size: 62px; display: block; }
  .units-flag .label { font-size: 34px; letter-spacing: 1px; display: block; margin-top: -4px; }
  .kicker {
    position: absolute; left: 76px; top: 48px;
    font-family: "Open Sans", sans-serif; font-size: 68px; color: var(--white); font-weight: 400;
  }
  .title {
    position: absolute; left: 124px; top: 128px;
    font-family: "Open Sans", sans-serif; font-weight: 700; font-size: 132px;
    letter-spacing: -2px; color: var(--white); line-height: 1.05;
  }
  .delivery {
    position: absolute; right: 66px; top: 284px;
    font-family: "Open Sans", sans-serif; font-style: italic; font-size: 48px; color: var(--white);
  }
  .features { position: absolute; left: 45px; top: 466px; list-style: none; }
  .features li {
    font-family: "Libre Baskerville", serif; font-weight: 700; font-size: 34px;
    color: var(--ink); line-height: 1.1; margin-bottom: 28px; display: flex;
  }
  .features .mark { color: var(--teal); width: 32px; flex: none; }
  .features .indent { display: block; padding-left: 98px; }
  .contact {
    position: absolute; right: 41px; top: 586px; text-align: right;
    font-family: "Roboto Condensed", sans-serif; font-weight: 700; color: var(--ink);
  }
  .contact .agents { font-size: 44px; line-height: 1; }
  .contact .phone { font-size: 102px; line-height: 1; margin-top: 8px; letter-spacing: -1px; }
  .contact .email { font-size: 46px; line-height: 1; margin-top: 8px; }
  .disclaimer {
    position: absolute; left: 53px; right: 53px; top: 832px;
    font-family: "Libre Baskerville", serif; font-size: 14.5px; line-height: 23px;
    color: var(--ink); text-align: justify;
  }
</style>
</head>
<body>
<main class="sign">
  <svg class="header-wave" viewBox="0 0 1200 460" aria-hidden="true">
    <path class="band" d="M0 0 H1200 V350 C1060 360 900 370 760 410 C620 450 470 450 330 415 C200 385 120 385 0 420 Z"/>
    <path class="corner" d="M945 0 H1200 V255 Z"/>
  </svg>
  <div class="units-flag"><span class="count">2</span><span class="label">UNITS AVAIL</span></div>

  <p class="kicker">Boutique Luxury</p>
  <h1 class="title">Condominiums</h1>
  <p class="delivery">Delivering late 2015</p>

  <ul class="features">
    <li><span class="mark">§</span>Luxury Finishes</li>
    <li><span class="mark">§</span>Designer Kitchens and Bath</li>
    <li><span class="mark">§</span>Each Unit over 2,000 sf</li>
    <li><span class="mark">§</span><span>Deeded Parking<span class="indent">with Each Unit</span></span></li>
  </ul>

  <div class="contact">
    <p class="agents">Marissa Talbot or Vernon Pike</p>
    <p class="phone">(202) 555-0147</p>
    <p class="email">Marissa.Talbot@example-realty.com</p>
  </div>

  <p class="disclaimer">These Condominium(s) have not been registered by the Office of Residential Standards and Property Oversight Bureau Tenancy Transition and Transfer Section. A Condominium Unit may be reserved on a non-binding reservation agreement, but no contract of sale or lease that is binding on the purchaser may be entered into prior to registration.</p>
</main>
</body>
</html>
```